Rackcard for That Dusty Granary event

We're a small nonprofit reuse center for home improvement supplies. We pick up donations of unwanted and salvaged building materials throughout the metro DC region. Then, we make the building materials available to the public at low cost, and provide vintage materials for restoring old homes. We also offer public education about reuse, and distribute free supplies to local nonprofits and neighbors in need.
Our free annual event, That Dusty Granary, is a old-timey fall festival that celebrates all things vintage (architectural salvage, restoring historic homes, antique appraisal, etc).
We're looking for a rackcard design for this year's event that will be used to invite the general public to our event. We usually prefer to stay away from photography in our flyers (as it can look very "stock image" cheesy), but we're interested in seeing any proposals you have.
Attached is the approved wording for our rackcard.
You can see more about Harbor Pallet at HarborPallet.org

Target Market(s)

Historic home owners, antique collectors/dealers, historic society members, local history buffs, architecture enthusiasts, families (all ages), folks who just like vintage stuff.

Industry/Entity Type

Non Profit

Font styles to use
Serif
Decorative
Script

Requirements
Must have
• Copy is preapproved and must be used exactly.
• Size of rackcard must be 5x7 inches. But can be landscape or portrait.
Nice to have
• See reference files for colors desired - these photos are for color suggestions, they're not intended to suggest design. Though they are very nice looking designs as well.
• Turquoise, browns, cedar, salmon, oranges, reds, etc.
• Antique house, architectural salvage, tools, etc. implied in the art work. Wood, old-fashioned wallpaper, skeleton keys, brick, and crown molding are some ideas.
• This is also a fall event, touches of an old-time fall festival would be nice.
Should not have
• We usually prefer to not use photos of people or places. Most flyers with photos look very "stock-photo" like and cheap. But, if you are extremely skilled with blending photos into an attractive event flyer then we're willing to take a look at all design options.
• I've attached some reference photos for ideas as well.

```html
<!DOCTYPE html>
<html lang="en">
<head>
<meta charset="utf-8">
<title>That Dusty Granary – Rackcard</title>
<link href="https://fonts.googleapis.com/css2?family=Kalam:wght@700&family=Parisienne&family=Alfa+Slab+One&family=Arimo:wght@700&display=swap" rel="stylesheet">
<style>
  :root{
    --wood-dark:#5a3519;
    --wood-mid:#8a5a30;
    --sign-light:#e9d3a6;
    --sign-mid:#d6b47c;
    --sign-edge:#a77a45;
    --ink-brown:#4b2c14;
    --accent-red:#c8201a;
    --badge-cream:#fdf3d8;
    --white:#ffffff;
    --wire:#8c8c8c;
  }
  html,body{margin:0;padding:0;overflow:hidden;}
  body{width:857px;height:1200px;position:relative;background:var(--wood-dark);}
  .rackcard{position:absolute;inset:0;width:857px;height:1200px;overflow:hidden;}
  .backdrop{
    position:absolute;inset:0;
    background:
      radial-gradient(ellipse at 15% 10%, #d9731f 0 14%, transparent 30%),
      radial-gradient(ellipse at 95% 60%, #e0a21e 0 10%, transparent 24%),
      radial-gradient(ellipse at 5% 75%, #e7a72a 0 12%, transparent 26%),
      radial-gradient(ellipse at 90% 96%, #d86a1c 0 10%, transparent 24%),
      linear-gradient(180deg, var(--wood-mid), var(--wood-dark) 60%, #4a2a12);
  }
  .hanger{position:absolute;inset:0;}
  .sign{
    position:absolute;left:70px;top:295px;width:700px;height:440px;
    background:linear-gradient(180deg,var(--sign-light),var(--sign-mid));
    border:6px solid var(--sign-edge);border-radius:10px;box-sizing:border-box;
    box-shadow:6px 10px 16px rgba(0,0,0,.45);
    transform:rotate(-1.5deg);
    text-align:center;color:var(--ink-brown);
  }
  .sign-title{
    font-family:"Kalam",cursive;font-size:64px;line-height:1;margin:92px 0 14px;
  }
  .sign-subtitle{
    font-family:"Kalam",cursive;font-size:42px;line-height:1.2;margin:0 24px;
  }
  .sign-divider{display:block;margin:8px auto 10px;}
  .venue{
    font-family:"Arimo",sans-serif;font-weight:700;color:var(--ink-brown);font-size:25px;line-height:1.45;margin:0;
  }
  .date-badge{
    position:absolute;left:655px;top:22px;width:190px;height:220px;border-radius:50%;
    background:var(--badge-cream);border:4px solid #c9a36a;box-sizing:border-box;
    box-shadow:4px 6px 12px rgba(0,0,0,.4);
    text-align:center;color:var(--accent-red);
    font-family:"Alfa Slab One",serif;
    display:flex;flex-direction:column;justify-content:center;
  }
  .date-badge .day{font-size:27px;}
  .date-badge .date{font-size:31px;line-height:1.1;}
  .date-badge .time{font-size:23px;}
  .featuring{
    position:absolute;left:0;right:0;top:722px;margin:0;text-align:center;
    font-family:"Parisienne",cursive;font-weight:400;color:var(--white);font-size:80px;line-height:96px;
    text-shadow:2px 3px 4px rgba(0,0,0,.5);
  }
  .highlights{
    position:absolute;left:130px;right:130px;top:840px;margin:0;text-align:center;
    font-family:"Arimo",sans-serif;font-weight:700;color:var(--white);font-size:27px;line-height:34px;
    text-shadow:2px 2px 3px rgba(0,0,0,.6);
  }
  .highlights .note{font-size:22px;}
  .contact{
    position:absolute;left:0;right:0;top:1082px;margin:0;text-align:center;
    font-family:"Alfa Slab One",serif;color:var(--accent-red);font-size:25px;line-height:36px;
    text-shadow:1px 1px 0 rgba(255,255,255,.35);
  }
</style>
</head>
<body>
<main class="rackcard">
  <div class="backdrop" role="img" aria-label="Rustic brown wood-plank background scattered with red, orange and yellow autumn maple leaves"></div>

  <svg class="hanger" width="857" height="1200" aria-hidden="true">
    <line x1="372" y1="32" x2="160" y2="305" stroke="var(--wire)" stroke-width="4"/>
    <line x1="372" y1="32" x2="690" y2="292" stroke="var(--wire)" stroke-width="4"/>
    <circle cx="372" cy="30" r="12" fill="#9d9d9d" stroke="#555" stroke-width="3"/>
  </svg>

  <div class="date-badge">
    <span class="day">SATURDAY</span>
    <span class="date">Sept. 12th,</span>
    <span class="time">10am – 3pm</span>
  </div>

  <section class="sign">
    <h1 class="sign-title">That Dusty Granary:</h1>
    <p class="sign-subtitle">A Celebration of Old Homes and<br>the Folks Who Love Them</p>
    <svg class="sign-divider" width="260" height="14" aria-hidden="true">
      <path d="M5 7 Q65 -2 130 7 T255 7" fill="none" stroke="var(--accent-red)" stroke-width="3"/>
    </svg>
    <p class="venue">at Harbor Pallet's Reuse Warehouse<br>1820 Millbrook Lane, Riverdale MD 20737<br>Just 5 min. from DC in the Hyattsville area!</p>
  </section>

  <h2 class="featuring">~ Featuring ~</h2>
  <p class="highlights">Antique Experts, Preservation &amp; Appraisal Advice,<br>and Free Workshops<br>Old-Timey Bands, Food, and Cider and a<br>Rare Opportunity to view our large<br>selection of Vintage Tools<br><span class="note">(normally sold only online)</span></p>

  <p class="contact">Questions? www.HarborPallet.org<br>301-555-0148 or Outreach@HarborPallet.org</p>
</main>
</body>
</html>
```